Digital Imaging Website Design Project

This project is for 3 page designs - The main Home page design, department page design & content page design which will utilize most of the home page components.

Client Background - http://www.kelvarprint.example

An almost Forty year old established printing company that has a large client base of architect/engineering, as the print shop opened up as a blueprinting company, and over the years has grown, changed and expanded to offer document and digital file management for this industry. KPRInc. has also always offered color printing services, but recently has expanded their color department to be able to offer amazing dimensional printing, and extreme cutting technology.

These new products and services will be targeted to new industries for repeatable printing needs, promotional, point of purchase color printing, as well as in-store, interior decor/wall. These new printing services are only offered by KPRINC in their area, and they want to convey that they are on the leading edge of color printing technology, while at the same time, not eliminating their existing primary business scaring away their traditional client base of architectural/engineering firms that use them for large format printing, scanning and document management services.

1 - Home Page Design
Primary Goals of the design:

1.Provide a new, eye catching engaging website that conveys the above expansion/growth/cutting edge company.
2.Full screen design please to move away from the 'center' bordered up website they currently have.
3.Design Components – We don't have any media to provide you with exception of our logo. We're looking for fresh design that is exciting and engaging imagery. Additionally, we are working on a color/effected version of our logo to place on the color division page, and this will probably tie in with the design you create for us.
4.It should be designed to be able to work as a responsive design as well so that when installed, will work across devices etc..
5.Colors – Same color scheme, but if you have an accent color you'd like to use to make the site pop, go for it!

Requirements:
1.The 4 divisions of the company should be the main feature so that the client depending on which department they are needing, will see those 4 choices clearly in the design, and they'll know to click on one of them to get more information and to their needed services.

2.The main goal of the site is to get visitors to place an order, there should be a feature on the home page for this call to action.

3.Put in an element that communicates the main benefit of KPRInc. - an area for a 1-line Statement/Call to Action / Overall Company Benefit/

4.The 4 divisions need to have eye catching elements related to their products and services, and that clearly illustrate that the user should click on that to go to the appropriate area for products and services

Reprographics
This department is specifically geared to architect/engineering industry
BYLine for optional Use: Partnering with Building Industry Providers since 1975
Related pages for better understanding:
http://www.kelvarprint.example/services/portland_professional_printing_services
http://www.kelvarprint.example/services/reprographics
Digital File Management
This department is related to Architect/engineers, but can also apply to any other industry needing electronic document management, scanning, or archival services.
BYLine for optional use: Effective & Efficient Digital Solutions at every level.
Related Pages:
http://www.kelvarprint.example/colorgraphics/electronic_file_document_management
http://www.kelvarprint.example/colorgraphics/document_scanning_service
http://www.kelvarprint.example/services/scanning_and_archiving

Color Graphics
This Department is newly expanded / has expanded services / they are focusing more of their efforts on this department and is a key reason for updated website design.
This Department image/representation should be stellar in the imagery to convey the excellence of the color department the services availble.
One of their newest products/services is dimensional printing – not 3-D, but raised element printing. Essentially a client could pick components on their graphic that that they want to 'bump' out, and additional layers would be put in place to create a popped out, dimensional effect. * Bonus points for creating the color department image that effectively conveys this new service – whether it's showing an abstract image/element that is actually raised off the page/paper/component. Additionally the color dimensional printing can be done on practically any material – glass, vinyl, material etc.... Please let me know if you have any questions on this.
BYLine for optional Use: See How Our Color Stands Out From the Rest
Related pages:
http://www.kelvarprint.example/colorgraphics
http://www.kelvarprint.example/colorgraphics/color_digital_imaging

Equipment & Supplies
This department provides specific supplies and hardware vs. printing products/services. Our largest client base is architects/engineers, but is not limited to this industry. Typical equipment is large printers, and supplies are typically paper products geared to the large format printing services, for the architect/engineers industry.
Byline for optional Use: In-House Printing & Fulfillment Services
Related pages:
http://www.kelvarprint.example/tervik_amlo_equipment_sales
http://www.kelvarprint.example/supplies

Additionally - Possibly have descriptive text sections below these 4 elements, but this is optional.

2.) Department/Division Page design -

This page should pull the home page element to over based on which division is selected.
Have a submenu design incorporated so that users can navigate to all the products and services that will be listed under that division
Contain a plugin design for FAQs – so that depending on which division page they are on, the appropriate FAQ's would display for use to have easy access to.
Contain a plugin design for – Contact Us easy form – short form –
Name
Company
Number
Email
Project Details/Questions: Text box

3.)Content Page design
This page should have main area for content
Area for an image with slideshow of other supporting images
Optional area for video – most (99%) of the pages will not have videos, but in the case we do, would like an area that will display videos effectively.
Optional FAQ plugin display
Contact plugin display

Global Elements:

Static and very visible site features that are in a position so that if user clicks beyond home page will still see these are:
Get a Quote
Place Order
Digital Plan-room
Call Today - 541-867-2290

Other global components:
SM Icons – QX, Chirply, ProNexa
Rotating Testimonial

Navigational Menu:
The KPR Difference
About
Sustainability
Products & Services
Reprograhics
Digital File Management
Color Graphics
Equipment & Supplies
Login
Blog
Contact Us

After the contest – What would be great to have is when a user clicks on one of the departments, it takes that visual element and continues onto it's department page for a smaller but related image - But this may be an after this web design contest.

Additionally will need some other design work on the interior pages, as well, so hoping to find a great designer to complete the other tasks – as well as be the go-to for future endeavors!

Thanks for looking at the project, and I look forward to any questions you may have.

Looking forward to hearing from interested designers! - If you're curious about my work, you can find my profile at:  https://www.freelanzo.example/users/~07b3e2c91f4d6a05

Please see description

```html
<!DOCTYPE html>
<html lang="en">
<head>
<meta charset="utf-8">
<title>Kelvar Print &amp; Reprographics — Home</title>
<link href="https://fonts.googleapis.com/css2?family=Open+Sans:wght@400;600;700&family=Oswald:wght@500;600&display=swap" rel="stylesheet">
<style>
:root{
  --navy:#2b4a7a;
  --navy-dark:#1f3866;
  --brand:#2a3a8c;
  --green:#8dc63f;
  --sky:#3fb8e0;
  --lavender:#8a8fe0;
  --yellow:#e9c12f;
  --ink:#333;
  --muted:#666;
  --light:#ededed;
  --footer:#333333;
  --white:#fff;
}
*{margin:0;padding:0;box-sizing:border-box}
html,body{width:687px;height:1200px;overflow:hidden}
body{position:relative;background:var(--white);font-family:"Open Sans",Arial,sans-serif;color:var(--ink);font-size:5px;line-height:1.45}
.abs{position:absolute}

/* header */
.site-header{position:absolute;left:0;top:0;width:687px;height:79px;background:var(--white)}
.brand{position:absolute;left:172px;top:14px;display:flex;align-items:center;gap:5px}
.brand-mark{width:24px;height:24px;border-radius:50%;background:var(--brand)}
.brand-name{font-weight:700;color:var(--brand);font-size:6px;line-height:1.15;width:80px;text-transform:uppercase}
.account{position:absolute;left:380px;top:9px;display:flex;align-items:center;gap:5px;font-size:4.5px;font-weight:600}
.signup{background:var(--green);color:var(--white);padding:3px 7px}
.call{position:absolute;left:442px;top:9px;font-size:5px;color:var(--muted)}
.call b{font-size:8.5px;color:var(--brand);font-weight:700;margin-left:2px}
.follow{position:absolute;left:447px;top:24px;display:flex;align-items:center;gap:3px;font-size:5px;color:var(--muted)}
.social-dot{width:10px;height:10px;border-radius:50%;background:#3a72b8}
.utility{position:absolute;left:406px;top:44px;display:flex;height:13px;background:#9aa1aa}
.utility span{color:var(--white);font-size:4px;padding:0 4px;line-height:13px;border-right:1px solid #b9bec5}
.main-nav{position:absolute;left:176px;top:64px;display:flex;gap:6.5px;font-size:4.6px;text-transform:uppercase}
.main-nav .current{color:var(--sky)}

/* hero */
.hero{position:absolute;left:0;top:79px;width:687px;height:253px;background:var(--navy)}
.hero h1{position:absolute;left:0;width:687px;top:6px;text-align:center;font-family:"Oswald",Impact,sans-serif;font-weight:600;color:var(--white);font-size:16px;line-height:23px;letter-spacing:.2px}
.hero h1 em{font-style:normal;color:var(--green)}
.hero .lead{position:absolute;left:190px;width:307px;top:56px;text-align:center;color:var(--white);font-size:6.2px;line-height:1.5}
.disc{position:absolute;border-radius:50%;border:4px solid var(--white);box-shadow:0 3px 8px rgba(0,0,0,.35)}
.hero-tag{position:absolute;z-index:5;height:19px;line-height:19px;padding:0 3px;background:var(--green);font-family:"Oswald",Impact,sans-serif;font-weight:500;font-size:11.5px;color:var(--ink);white-space:nowrap}
.dots{position:absolute;display:flex;gap:2px}
.dots i{width:4px;height:4px;border-radius:50%;background:#cfd6e0;border:0.5px solid #888}
.dots i.on{background:var(--white)}

/* divisions */
.section-title{font-size:8px;font-weight:600;text-transform:uppercase;color:var(--ink);text-align:center}
.intro{text-align:center;color:var(--muted);font-size:5px}
.division{position:absolute;width:86px;text-align:center}
.division .icon{width:50px;height:50px;border-radius:50%;margin:0 auto;display:flex;align-items:center;justify-content:center}
.division h3{font-size:6.5px;font-weight:400;margin-top:7px;color:var(--ink)}
.division p{width:70px;margin:5px auto 0;font-size:4.8px;color:var(--muted);line-height:1.6}

/* about & products */
.about{position:absolute;left:0;top:512px;width:687px;height:137px;background:linear-gradient(180deg,#f2f2f2,#e4e4e4)}
.block-title{font-size:8px;font-weight:400;text-transform:uppercase;color:var(--ink)}
.body-copy{font-size:4.6px;color:var(--muted);line-height:1.55}
.more{display:inline-block;width:6px;height:6px;background:var(--navy)}
.products{position:absolute;left:0;top:649px;width:687px;height:131px;background:var(--white)}

/* cta band */
.cta-band{position:absolute;left:0;top:780px;width:687px;height:56px;background:var(--light)}
.cta{position:absolute;top:16px;width:83px;height:26px;color:var(--white);font-size:6.5px;text-transform:uppercase;display:flex;align-items:center;justify-content:center}
.cta.quote{left:187px;background:var(--navy-dark)}
.cta.order{left:302px;background:var(--sky)}
.cta.planroom{left:416px;background:var(--lavender)}
.cta-divider{position:absolute;top:10px;width:1px;height:36px;background:#d3d3d3}

/* testimonials */
.testimonials{position:absolute;left:0;top:836px;width:687px;height:176px;background:var(--yellow)}
.quote-item{position:absolute;width:86px;text-align:center}
.avatar{width:50px;height:50px;border-radius:50%;margin:0 auto;border:3px solid var(--white);background:linear-gradient(160deg,#d8d2c8,#8f8378)}
.quote-item p{width:74px;margin:10px auto 0;font-size:4.6px;color:var(--ink);line-height:1.55}

/* blog */
.blog{position:absolute;left:0;top:1012px;width:687px;height:128px;background:var(--white)}
.post{position:absolute;top:40px;display:flex;gap:10px}
.post-thumb{position:relative;width:56px;height:56px;border-radius:50%;flex:none}
.post-date{position:absolute;right:-4px;bottom:-2px;width:20px;height:20px;border-radius:50%;background:var(--navy);color:var(--white);font-size:3.5px;text-align:center;padding-top:5px;line-height:1.2}
.post h4{font-size:6px;font-weight:400;line-height:1.35;width:95px}
.post p{font-size:4.6px;color:var(--muted);margin-top:4px;width:100px;line-height:1.55}

/* footer */
.site-footer{position:absolute;left:0;top:1140px;width:687px;height:60px;background:var(--footer);color:#bbb;font-size:4.6px}
.foot-col{position:absolute;top:12px;line-height:9.6px}
.foot-col li{list-style:none}
.foot-col li::before{content:"›";margin-right:4px;color:#888}
.foot-social{position:absolute;left:429px;top:12px}
.foot-social .row{display:flex;gap:3px;margin-top:4px}
.foot-social .row i{width:10px;height:10px;border-radius:50%;background:#777}
</style>
</head>
<body>

<header class="site-header">
  <div class="brand">
    <div class="brand-mark"></div>
    <div class="brand-name">Kelvar Print &amp; Reprographics Company, Inc.</div>
  </div>
  <div class="account"><span>LOG IN OR</span><span class="signup">SIGN UP</span></div>
  <div class="call">Call Today: <b>541-867-2290</b></div>
  <div class="follow">Follow us On: <i class="social-dot"></i><i class="social-dot" style="background:#36a9e1"></i><i class="social-dot" style="background:#2a6fa8"></i></div>
  <div class="utility"><span>THE KPR DIFFERENCE</span><span>BLOG</span><span style="border:0">CONTACT US</span></div>
  <nav class="main-nav">
    <span>About</span><span class="current">Sustainability</span><span>Products &amp; Services</span><span>Reprographics</span><span>Digital File Management</span><span>Color Graphics</span><span>Equipment &amp; Supplies</span>
  </nav>
</header>

<section class="hero">
  <h1>ACCESS TO THE LARGEST NETWORK OF DIGITALLY<br>CONNECTED <em>REPROGRAPHICS FIRMS</em></h1>
  <p class="lead">Kelvar Print &amp; Reprographics (KP&amp;R) is a full service reprographics company serving Oregon and Southwest Washington's design and building community.</p>
  <div class="disc" role="img" aria-label="Photo of architectural blueprints and drawings" style="left:178px;top:86px;width:132px;height:142px;border-radius:50%;background:linear-gradient(135deg,#e6eef4,#9fb6c8)"></div>
  <div class="disc" role="img" aria-label="Photo of a precision cutting machine" style="left:377px;top:86px;width:132px;height:142px;background:linear-gradient(135deg,#f3efe8,#c9b9a3)"></div>
  <div class="disc" role="img" aria-label="Photo of colorful printed swatches" style="left:274px;top:86px;width:140px;height:142px;background:linear-gradient(135deg,#e85a4f,#f2b84b 45%,#5aa0d8)"></div>
  <span class="hero-tag" style="left:192px;top:136px">REPROGRAPHIC</span>
  <span class="hero-tag" style="left:216px;top:160px">SERVICES</span>
  <span class="hero-tag" style="left:311px;top:136px">COLOR PRINTING</span>
  <span class="hero-tag" style="left:344px;top:160px">SERVICES</span>
  <span class="hero-tag" style="left:442px;top:136px">CUTTING</span>
  <span class="hero-tag" style="left:422px;top:160px">TECHNOLOGY</span>
  <div class="dots" style="left:335px;top:243px"><i></i><i class="on"></i><i></i></div>
</section>

<section class="abs" style="left:0;top:332px;width:687px;height:180px">
  <h2 class="section-title abs" style="left:0;width:687px;top:16px">Taking to look at our variable process</h2>
  <p class="intro abs" style="left:180px;width:327px;top:28px">At Kelvar Print and Reprographics we provide a wide array of services involving document imaging and duplication as well as online and offline document management and archiving services.</p>

  <div class="division" style="left:171px;top:60px">
    <div class="icon" style="background:#eec22e"><svg width="26" height="26" viewBox="0 0 26 26" fill="none" stroke="#fff" stroke-width="2"><path d="M4 22V4l18 18z"/><path d="M9 17v-5l5 5z"/></svg></div>
    <h3>Reprographics</h3>
    <p>This department is specifically geared to architect/engineering industry BYLine for optional Use: Partnering with Building</p>
  </div>
  <div class="division" style="left:257px;top:60px">
    <div class="icon" style="background:#3fb8e0"><svg width="26" height="26" viewBox="0 0 26 26" fill="none" stroke="#fff" stroke-width="2"><rect x="7" y="7" width="12" height="12"/><path d="M10 3v4M13 3v4M16 3v4M10 19v4M13 19v4M16 19v4M3 10h4M3 13h4M3 16h4M19 10h4M19 13h4M19 16h4"/></svg></div>
    <h3>Digital File Management</h3>
    <p>This department is related to Architect/engineers, but can also apply to any other industry needing electronic...</p>
  </div>
  <div class="division" style="left:343px;top:60px">
    <div class="icon" style="background:#8dc63f"><svg width="26" height="26" viewBox="0 0 26 26" fill="#fff"><path d="M5 12l8-8 8 8-8 8z"/><path d="M21 15c0 2-1 4-2 4s-2-2-2-4l2-3z"/></svg></div>
    <h3>Color Graphics</h3>
    <p>This Department is newly expanded / has expanded services / they are focusing more of their efforts on this...</p>
  </div>
  <div class="division" style="left:429px;top:60px">
    <div class="icon" style="background:#8a8fe0"><svg width="26" height="26" viewBox="0 0 26 26" fill="none" stroke="#fff" stroke-width="2"><ellipse cx="14" cy="15" rx="7" ry="8" transform="rotate(35 14 15)"/><path d="M10 9c-3-3-6-2-6 1"/></svg></div>
    <h3>Equipment &amp; Supplies</h3>
    <p>This department provides specific supplies and hardware vs. printing products/services. Our largest client base is...</p>
  </div>
</section>

<section class="about">
  <h2 class="block-title abs" style="left:172px;top:16px">About Kelvar Print</h2>
  <div class="abs" style="left:172px;top:29px;width:340px">
    <p class="body-copy"><b style="color:var(--navy)">Kelvar Print &amp; Reprographics (KP&amp;R)</b> is a full service reprographics company serving Oregon and Southwest Washington's design and building community. Founded in 1975 by Daniel Orsen, we utilize the latest digital technologies to provide a wide range of reprographics and graphic imaging services. Our services range from electronic document management, color digital imaging, photocopying, cad plotting, and high-speed large format printing. We have evolved from a "print and deliver" provider to become the leader in information management and production.</p>
    <p class="body-copy" style="margin-top:4px">Our On-Site programs provide staffed and un-staffed production centers at client sites for maximum efficiency and cost recovery.<br>We are authorized resellers for industry leading equipment and supplies for the design and building market.</p>
    <span class="more" style="margin-top:3px"></span>
  </div>
  <div class="abs" role="img" aria-label="Illustration of drafting compass, pencils and ruler" style="left:375px;top:64px;width:140px;height:70px;background:linear-gradient(160deg,rgba(230,200,150,.0),#d9b77e 60%,#a8a8a8);clip-path:polygon(10% 100%,100% 10%,100% 40%,45% 100%)"></div>
</section>

<section class="products">
  <h2 class="block-title abs" style="left:172px;top:38px">Our Product &amp; Services</h2>
  <div class="abs" style="left:172px;top:51px;width:200px">
    <p class="body-copy">At Kelvar Print &amp; Reprographics we provide a wide array of services involving document imaging and duplication as well as online and offline document management and archiving services.</p>
    <p class="body-copy" style="margin-top:4px">Please select your area of interest from the menu choices. If you do not find the information that you need, please email us or contact us by phone at (541) 867-2290.</p>
    <span class="more" style="margin-top:3px"></span>
  </div>
  <div class="abs" role="img" aria-label="Photo of a technician checking a color print with a loupe" style="left:382px;top:14px;width:110px;height:110px;border-radius:50%;border:4px solid #fff;box-shadow:0 2px 8px rgba(0,0,0,.3);background:linear-gradient(150deg,#c9b3a0,#6d7b8a 60%,#2d2d2d)"></div>
</section>

<section class="cta-band">
  <div class="cta quote">Get a Quote</div>
  <div class="cta-divider" style="left:286px"></div>
  <div class="cta order">Place Order</div>
  <div class="cta-divider" style="left:400px"></div>
  <div class="cta planroom">Digital Plan-Room</div>
</section>

<section class="testimonials">
  <h2 class="block-title abs" style="left:172px;top:16px">Testimonials</h2>
  <div class="quote-item" style="left:173px;top:38px"><div class="avatar" role="img" aria-label="Client portrait"></div><p>Lorem ipsum dolor sit amet, consectetur adipisicing elit, sed do eiusmod tempor incididunt ut labore et dolore magna</p></div>
  <div class="quote-item" style="left:257px;top:38px"><div class="avatar" role="img" aria-label="Client portrait"></div><p>Lorem ipsum dolor sit amet, consectetur adipisicing elit, sed do eiusmod tempor incididunt ut labore et dolore magna</p></div>
  <div class="quote-item" style="left:343px;top:38px"><div class="avatar" role="img" aria-label="Client portrait"></div><p>Lorem ipsum dolor sit amet, consectetur adipisicing elit, sed do eiusmod tempor incididunt ut labore et dolore magna</p></div>
  <div class="quote-item" style="left:428px;top:38px"><div class="avatar" role="img" aria-label="Client portrait"></div><p>Lorem ipsum dolor sit amet, consectetur adipisicing elit, sed do eiusmod tempor incididunt ut labore et dolore magna</p></div>
  <div class="dots" style="left:333px;top:159px"><i class="on"></i><i></i><i></i><i></i></div>
</section>

<section class="blog">
  <h2 class="block-title abs" style="left:172px;top:18px">Latest Blog</h2>
  <article class="post" style="left:172px">
    <div class="post-thumb" role="img" aria-label="Photo of students studying together" style="background:linear-gradient(150deg,#e8a3a0,#8a5a4a)"><span class="post-date">AUG 16<br>2013</span></div>
    <div><h4>Lorem ipsum dolor sit amet consectetur adipisicing elit</h4><p>Lorem ipsum dolor sit amet, consectetur adipisicing elit, sed do eiusmod tempor incididunt ut labore et dolore magna aliqua Ut enim ad minim veniam...</p></div>
  </article>
  <article class="post" style="left:354px">
    <div class="post-thumb" role="img" aria-label="Photo of a red paint brush stroke" style="background:linear-gradient(150deg,#f3e6e6,#c8283a)"><span class="post-date">AUG 16<br>2013</span></div>
    <div><h4>Lorem ipsum dolor sit amet consectetur adipisicing elit</h4><p>Lorem ipsum dolor sit amet, consectetur adipisicing elit, sed do eiusmod tempor incididunt ut labore et dolore magna aliqua minim veniam.</p></div>
  </article>
</section>

<footer class="site-footer">
  <ul class="foot-col" style="left:172px"><li>The KPR Difference</li><li>About</li><li>Sustainability</li><li>Products &amp; Services</li></ul>
  <ul class="foot-col" style="left:262px"><li>Reprographics</li><li>Digital File Management</li><li>Color Graphics</li><li>Equipment &amp; Supplies</li></ul>
  <ul class="foot-col" style="left:352px"><li>Login</li><li>Blog</li><li>Contact Us</li></ul>
  <div class="foot-social">Follow us On:<div class="row"><i></i><i></i><i></i></div><div style="margin-top:8px">Copyright © 2013 KPR</div></div>
</footer>

</body>
</html>
```